Flat Belly Design Graphics for Social

I want to create 9 social media graphics (new Instagram size 4:5 (1080 x 1350 pixels) focusing on our Flat Belly Graphics, using the pics attached. Use the attached pics, NO RANDOM STOCK PHOTOGRAPHY. For the color scheme of the graphics, the color palette is attached. YOU MUST POST ALL 9 GRAPHICS IN ONE ENTRY.
Using the 3 titles below, create one set of graphics. 1) with all text, then for the others, use the pictures as detailed below in IMPORTANT:
1. 21-Night Lean Middle Reboot Beyond 50
2. The 20-Second Trim-Core Menu Guide
3. Starlet Tricks to a Slender Midline Beyond 50 - Zero Scalpel Needed
IMPORTANT:
Only use RK Pic 1 and RK Pic 2 with the title, 21-Night Lean Middle Reboot Beyond 50
Only use meal plan1 and meal plan2 pics with the title, 20-Second Trim-Core Menu Guide
Only use starlet tricks 1 and starlet tricks 2 pics with the title, Starlet Tricks to a Slender Midline Beyond 50 - Zero Scalpel Needed
women over 40

```html
<!DOCTYPE html>
<html lang="en">
<head>
<meta charset="utf-8">
<title>Lean Middle Social Set</title>
<link href="https://fonts.googleapis.com/css2?family=Oswald:wght@500;600;700&display=swap" rel="stylesheet">
<style>
:root{
  --board:#5b5b5b;
  --forest:#2f4c4a;
  --forest-glass:rgba(47,76,74,.93);
  --rose:#e597b2;
  --blush:#f7dbe2;
  --petal:#f9dfe4;
  --white:#ffffff;
  --sky:#5ec3d8;
  --walnut:#6b3f2a;
}
*{box-sizing:border-box;margin:0;padding:0}
html,body{width:967px;height:1200px;overflow:hidden;background:var(--board)}
body{position:relative;font-family:'Oswald',Arial Narrow,sans-serif;font-weight:600;text-transform:uppercase;line-height:.95}
.tile{position:absolute;width:295px;height:368px;overflow:hidden}
.col-a{left:12px}.col-b{left:333px}.col-c{left:656px}
.row-a{top:8px}.row-b{top:415px}.row-c{top:817px}
.photo{position:absolute;inset:0}
.produce{background:radial-gradient(circle at 20% 25%,#e8b23a 0,transparent 30%),radial-gradient(circle at 25% 80%,#d9432e 0,transparent 30%),radial-gradient(circle at 80% 85%,#c53a2a 0,transparent 25%),linear-gradient(135deg,#4a3a2c,#3b2e24 60%,#5a3c2c)}
.produce-alt{background:radial-gradient(circle at 20% 20%,#e06a4a 0,transparent 30%),radial-gradient(circle at 15% 75%,#c93b2c 0,transparent 28%),radial-gradient(circle at 85% 85%,#d99a3a 0,transparent 28%),linear-gradient(135deg,#3f3328,#2f2a22)}
.produce-frame{background:linear-gradient(90deg,#c6402e,#7b5a3a 18%,#3b3026 40%,#3b3026 60%,#6d8a3a 82%,#e0a13a)}
.friends{background:linear-gradient(180deg,#f3efea 0,#c89a7e 40%,#6a4a3a 70%,#3a2f2b 100%)}
.friends-sky{background:linear-gradient(90deg,var(--sky) 0,#d8b9a8 35%,#c9a38c 55%,var(--sky) 100%)}
.coach{position:absolute;left:50%;transform:translateX(-50%);width:200px;height:330px;bottom:0;border-radius:90px 90px 10px 10px;background:linear-gradient(180deg,#2b2320 0,#6e4a38 25%,#f1eeee 45%,#ece8e6 100%)}
.kitchen{background:linear-gradient(180deg,#5c3526 0,#7a4a33 40%,#a98064 55%,#6b3f2a 75%,#4a2a1d 100%)}
.petal{background:var(--petal)}
.panel{position:absolute;background:var(--forest-glass);display:flex;flex-direction:column}
.panel.right{left:128px;top:20px;right:0;bottom:0;align-items:flex-end;padding:18px 18px 0 0;text-align:right}
.panel.center{left:58px;width:177px;top:48px;bottom:0;align-items:center;padding-top:20px;text-align:center}
.w{color:var(--white)}.b{color:var(--blush)}.r{color:var(--rose)}.f{color:var(--forest)}
.t-night{font-size:36px}
.t-lean{font-size:76px;font-weight:700}
.t-reboot{font-size:20px;margin-top:4px}
.t-beyond{font-size:44px;font-weight:700;margin-top:4px}
.t-fifty{font-size:96px;font-weight:700}
.fade{position:absolute;left:0;right:0;bottom:0;background:linear-gradient(180deg,rgba(47,76,74,0) 0,var(--forest) 50px);padding:60px 24px 20px}
.fade .lg{font-size:30px}
.fade .md{font-size:33px}
.fade .sm{font-size:24px}
.fade .xl{font-size:58px;font-weight:700}
.side-box{position:absolute;left:121px;top:32px;width:174px;height:302px;background:rgba(47,76,74,.9);padding:14px 10px 0 14px}
.side-box .a{font-size:31px}.side-box .b2{font-size:40px;font-weight:700}.side-box .c{font-size:30px}.side-box .d{font-size:24px}
.arch{position:absolute;left:0;right:0;bottom:0;height:165px}
.arch svg{position:absolute;inset:0}
.arch-text{position:absolute;left:0;right:0;bottom:18px;text-align:center}
.arch-text .s{font-size:32px}.arch-text .l{font-size:40px;font-weight:700}
.menu-head{position:absolute;left:0;right:0;top:198px;text-align:center}
.menu-head .s{font-size:22px}.menu-head .m{font-size:28px;font-weight:700}
.menu-block{position:absolute;left:83px;width:128px;top:244px;bottom:0;background:linear-gradient(180deg,rgba(47,76,74,0) 0,var(--forest) 30px);text-align:center;padding-top:6px}
.menu-block span{display:block;font-size:50px;font-weight:700;line-height:1}
</style>
</head>
<body>

<section class="tile col-a row-a">
  <div class="photo produce" role="img" aria-label="Flat-lay of fresh produce, meat and a meal plan notepad on dark wood"></div>
  <div class="panel right">
    <span class="t-night r">21-Night</span><span class="t-lean r">Lean</span><span class="t-reboot w">Middle Reboot</span><span class="t-beyond w">Beyond</span><span class="t-fifty b">-50-</span>
  </div>
</section>

<section class="tile col-b row-a">
  <div class="photo produce-alt" role="img" aria-label="Flat-lay of salmon, avocado, tomatoes, eggs and lentils on dark wood"></div>
  <div class="panel right">
    <span class="t-night r">21-Night</span><span class="t-lean r">Lean</span><span class="t-reboot w">Middle Reboot</span><span class="t-beyond w">Beyond</span><span class="t-fifty b">-50-</span>
  </div>
</section>

<section class="tile col-c row-a">
  <div class="photo produce-frame" role="img" aria-label="Fresh vegetables, fruit, salmon and legumes framing the sides"></div>
  <div class="panel center">
    <span class="t-night b">21-Night</span><span class="t-lean b">Lean</span><span class="t-reboot r">Middle Reboot</span><span class="t-beyond r">Beyond</span><span class="t-fifty r">-50-</span>
  </div>
</section>

<section class="tile col-a row-b">
  <div class="photo friends" role="img" aria-label="Two women sharing a whispered secret, one looking surprised"></div>
  <div class="fade">
    <div class="lg r">Starlet Tricks</div><div class="md w">To a Slender Midline</div><div class="sm w">Beyond 50-Zero Scalpel</div><div class="sm w">Needed</div>
  </div>
</section>

<section class="tile col-b row-b">
  <div class="photo friends" role="img" aria-label="Two women sharing a whispered secret, one looking surprised"></div>
  <div class="fade">
    <div class="lg r">Starlet Tricks</div><div class="sm w" style="font-size:30px">To a Slender Midline</div><div class="xl b">Beyond 50</div><div class="sm w">Zero Scalpel Needed</div>
  </div>
</section>

<section class="tile col-c row-b">
  <div class="photo friends-sky" role="img" aria-label="Two women on a blue backdrop, one whispering, one excited"></div>
  <div class="side-box">
    <div class="a r">Starlet</div><div class="b2 r">Tricks</div><div class="b2 b">To A</div><div class="c b">Slender</div><div class="c b">Midline</div><div class="c b">Beyond 50</div><div class="d b">Zero Scalpel</div><div class="c b">Needed</div>
  </div>
</section>

<section class="tile col-a row-c petal">
  <div class="coach" role="img" aria-label="Smiling woman in a white cropped sweater pointing down"></div>
  <div class="arch">
    <svg viewBox="0 0 295 165" preserveAspectRatio="none"><path d="M0 30 Q147 -25 295 30 V165 H0 Z" fill="var(--forest)"/></svg>
    <div class="arch-text"><div class="s b">The 20-Second</div><div class="l r">Trim-Core</div><div class="l r">Menu Guide</div></div>
  </div>
</section>

<section class="tile col-b row-c petal">
  <div class="coach" role="img" aria-label="Smiling woman in a white sweater pointing down"></div>
  <div class="menu-head"><div class="s f">The 20-Second</div><div class="m f">Trim-Core</div></div>
  <div class="menu-block"><span class="r">Menu</span><span class="r">Guide</span></div>
</section>

<section class="tile col-c row-c">
  <div class="photo kitchen" role="img" aria-label="Modern kitchen with wood cabinets and marble backsplash"></div>
  <div class="coach" role="img" aria-label="Smiling woman in a white sweater pointing down"></div>
  <div class="menu-head"><div class="s f">The 20-Second</div><div class="m f">Trim-Core</div></div>
  <div class="menu-block"><span class="r">Menu</span><span class="r">Guide</span></div>
</section>

</body>
</html>
```